Menu Re-Design for The Marlowbrook a british eatery in spanish holiday resort

Looking for a new design for our breakfast and lunch menu....

I have included some pictures of a few menus I like the feel of File No 1,2,3,4,5..... but am open to any ideas you may have....

The menu is to be double sided consisting of a front design with actual menu on reverse....

I have also included the relevant text files you will require...

We do not have a logo or set colour scheme to follow...

Target Market(s)

Predominantly British holidaymakers in popular Spanish resort....

Requirements
Must have
• Menu to be A3 and double sided, split between either a front page design and menu on reverse, or menu divided between both sides....
• Company Name:- The Marlowbrook
Nice to have
• Fun and Bold design whilst maintaining a feel of quality....
Should not have
• Please avoid the use of any food photography....

```html
<!DOCTYPE html>
<html lang="en">
<head>
<meta charset="utf-8">
<title>The Marlowbrook – Breakfast &amp; Lunch Menu</title>
<link rel="stylesheet" href="https://fonts.googleapis.com/css2?family=Patrick+Hand&family=Sniglet:wght@400;800&family=Open+Sans:wght@400;600&display=swap">
<style>
  :root{
    --backdrop:#d5dcdb;
    --paper:#f3f1e6;
    --mint:#3cbf98;
    --coral:#e7706a;
    --ink:#7a7263;
    --ink-soft:#a49c8c;
  }
  *{box-sizing:border-box;margin:0;padding:0}
  html,body{width:1200px;height:800px;overflow:hidden}
  body{background:var(--backdrop);position:relative;font-family:"Open Sans",sans-serif;color:var(--ink)}
  .page{position:absolute;background:var(--paper);box-shadow:0 2px 6px rgba(0,0,0,.12)}
  .menu-sheet{left:20px;top:20px;width:537px;height:760px}
  .cover{top:202px;width:280px;height:396px}
  .cover--cloche{left:590px}
  .cover--pattern{left:895px}
  .block{position:absolute}
  .art{position:absolute;border-radius:6px}
  .sheet-title{position:absolute;left:95px;top:18px;font-family:"Patrick Hand",cursive;font-size:42px;color:var(--mint);font-weight:400}
  .heading{font-family:"Sniglet",sans-serif;font-weight:800;color:var(--mint);font-size:14px;letter-spacing:.5px;text-transform:uppercase;margin-bottom:3px}
  .heading--script{font-family:"Patrick Hand",cursive;font-weight:400;text-transform:none;font-size:22px}
  .heading--big{font-size:34px}
  .dish{display:flex;justify-content:space-between;font-size:7.5px;line-height:11px;color:var(--ink)}
  .dish b{font-family:"Sniglet",sans-serif;font-weight:800;color:var(--mint);font-size:10px;text-transform:uppercase}
  .note{font-size:7px;color:var(--coral);margin-top:2px}
  .cover-title{position:absolute;left:0;right:0;text-align:center;font-family:"Sniglet",sans-serif;color:var(--mint)}
  .cover-name{font-weight:800;font-size:20px;text-transform:uppercase}
  .cover-sub{font-size:11px;text-transform:uppercase;letter-spacing:1px}
  .cover-menu{font-weight:800;font-size:44px;line-height:44px;letter-spacing:2px}
  .cover-hours{font-family:"Patrick Hand",cursive;font-size:16px}
  .badge{position:absolute;left:50px;top:108px;width:180px;height:180px;border-radius:50%;background:var(--paper);border:3px solid var(--mint)}
  .badge .cover-title{position:static}
  .badge-inner{position:absolute;inset:0;display:flex;flex-direction:column;align-items:center;justify-content:center}
  .badge .cover-name{font-size:16px}
  .badge .cover-menu{font-size:36px;line-height:38px}
</style>
</head>
<body>

<section class="page menu-sheet">
  <h1 class="sheet-title">Breakfast &amp; Lunch</h1>
  <div class="art" role="img" aria-label="Drawn teapot and cup" style="left:445px;top:8px;width:75px;height:70px;background:radial-gradient(circle,#eb8c86,#f3f1e6 72%)"></div>

  <div class="art" role="img" aria-label="Drawn fried egg and sausage" style="left:20px;top:78px;width:115px;height:120px;background:radial-gradient(circle at 40% 40%,#e7706a 0 14%,#e6e2d4 30%,#f3f1e6 70%)"></div>

  <div class="block" style="left:142px;top:80px;width:155px">
    <div class="dish"><b>Marlowbrook</b><span>5.50</span></div>
    <div class="dish"><span>Bacon, egg, sausage, beans, toast</span></div>
    <div class="dish"><b>Hearty</b><span>7.50</span></div>
    <div class="dish"><span>Two of each, tea or coffee</span></div>
    <div class="note">Ask about our veggie option</div>
  </div>

  <div class="block" style="left:310px;top:80px;width:207px">
    <div class="heading">Breakfast Snacks</div>
    <div class="dish"><span>Toast &amp; Jam</span><span>1.50</span></div>
    <div class="dish"><span>Beans on Toast</span><span>2.50</span></div>
    <div class="dish"><span>Egg on Toast</span><span>2.50</span></div>
    <div class="dish"><span>Bacon Roll</span><span>3.00</span></div>
    <div class="dish"><span>Sausage Roll</span><span>3.00</span></div>
    <div class="dish"><span>Egg Sandwich</span><span>3.00</span></div>
    <div class="dish"><span>Bacon &amp; Egg Roll</span><span>3.50</span></div>
  </div>

  <div class="art" role="img" aria-label="Drawn slices of toast" style="left:225px;top:200px;width:75px;height:70px;background:linear-gradient(135deg,#e2ddcd,#f3f1e6)"></div>

  <div class="block" style="left:20px;top:210px;width:200px">
    <div class="heading heading--script">Something Different?</div>
    <div class="dish"><b>Eggs Benedict</b><span>5.50</span></div>
    <div class="dish"><b>Eggs Royale</b><span>6.00</span></div>
    <div class="dish"><b>Pancake Stack</b><span>4.50</span></div>
    <div class="dish"><b>Smoked and Scrambled</b><span>6.00</span></div>
    <div class="dish"><b>Big Breakfast Wrap</b><span>5.00</span></div>
    <div class="dish"><b>Big Breakfast Muffin</b><span>4.50</span></div>
  </div>

  <div class="block" style="left:310px;top:250px;width:207px">
    <div class="heading">Omelettes</div>
    <div class="dish"><span>Plain</span><span>4.00</span></div>
    <div class="dish"><span>Cheese</span><span>4.50</span></div>
    <div class="dish"><span>Ham &amp; Cheese</span><span>5.00</span></div>
    <div class="dish"><span>Mushroom</span><span>4.50</span></div>
    <div class="dish"><span>Bacon &amp; Onion</span><span>5.00</span></div>
    <div class="note">Served with salad and chips</div>
  </div>

  <div class="block" style="left:150px;top:385px;width:205px">
    <div class="heading heading--big">Burgers</div>
    <div class="dish"><span>Quarter Pounder</span><span>5.50</span></div>
    <div class="dish"><span>Cheese Burger</span><span>6.00</span></div>
    <div class="dish"><span>Chicken Burger</span><span>6.00</span></div>
    <div class="dish"><span>Veggie Burger</span><span>5.50</span></div>
    <div class="note">All served with chips and salad</div>
  </div>
  <div class="art" role="img" aria-label="Drawn burger" style="left:20px;top:410px;width:120px;height:105px;background:radial-gradient(circle,#ddd7c6,#f3f1e6 70%)"></div>

  <div class="block" style="left:370px;top:385px;width:147px">
    <div class="heading">Wraps</div>
    <div class="dish"><b>BBQ</b><span>5.00</span></div>
    <div class="dish"><b>Cajun</b><span>5.00</span></div>
    <div class="dish"><b>Tikka</b><span>5.00</span></div>
    <div class="dish"><b>Sweet Chilli</b><span>5.00</span></div>
    <div class="dish"><b>Garlic</b><span>5.00</span></div>
  </div>

  <div class="art" role="img" aria-label="Drawn baguette sandwich" style="left:150px;top:525px;width:160px;height:45px;background:linear-gradient(90deg,#f3f1e6,#ddd7c6,#f3f1e6)"></div>

  <div class="block" style="left:340px;top:510px;width:177px">
    <div class="heading">Lite Bites &amp; Sides</div>
    <div class="dish"><span>Bowl of Chips</span><span>2.00</span></div>
    <div class="dish"><span>Cheesy Chips</span><span>2.50</span></div>
    <div class="dish"><span>Garlic Bread</span><span>2.50</span></div>
    <div class="dish"><span>Onion Rings</span><span>2.50</span></div>
    <div class="dish"><span>Chicken Nuggets</span><span>3.50</span></div>
    <div class="dish"><span>Soup of the Day</span><span>3.50</span></div>
  </div>

  <div class="block" style="left:20px;top:525px;width:125px">
    <div class="heading">Sandwiches</div>
    <div class="dish"><span>Ham Salad</span><span>3.50</span></div>
    <div class="dish"><span>Cheese &amp; Pickle</span><span>3.50</span></div>
    <div class="dish"><span>Tuna Mayo</span><span>3.50</span></div>
    <div class="dish"><span>BLT</span><span>4.00</span></div>
  </div>

  <div class="block" style="left:150px;top:585px;width:180px">
    <div class="heading">Fresh Baked Baguettes</div>
    <div class="dish"><span>Chicken &amp; Bacon</span><span>5.00</span></div>
    <div class="dish"><span>Tuna Melt</span><span>5.00</span></div>
    <div class="dish"><span>Steak &amp; Onion</span><span>6.00</span></div>
  </div>

  <div class="block" style="left:20px;top:640px;width:125px">
    <div class="heading">Jacket Potatoes</div>
    <div class="dish"><span>Beans</span><span>4.00</span></div>
    <div class="dish"><span>Cheese</span><span>4.00</span></div>
    <div class="dish"><span>Tuna Mayo</span><span>4.50</span></div>
    <div class="dish"><span>Chilli</span><span>5.00</span></div>
  </div>

  <div class="block" style="left:150px;top:675px;width:180px">
    <div class="heading">Salads</div>
    <div class="dish"><span>Chicken Caesar</span><span>6.00</span></div>
    <div class="dish"><span>Greek Salad</span><span>5.50</span></div>
    <div class="dish"><span>Tuna Nicoise</span><span>6.00</span></div>
  </div>

  <div class="art" role="img" aria-label="Drawn pizza slice and herbs" style="left:425px;top:655px;width:95px;height:95px;background:radial-gradient(circle,#d6cfbd,#f3f1e6 70%)"></div>
</section>

<section class="page cover cover--cloche">
  <div class="art" role="img" aria-label="Drawn serving cloche" style="left:95px;top:30px;width:90px;height:70px;background:radial-gradient(ellipse at 50% 80%,#bdb4a2,#f3f1e6 70%)"></div>
  <div class="cover-title" style="top:105px">
    <div class="cover-name">The Marlowbrook</div>
    <div class="cover-sub">Breakfast &amp; Lunch</div>
    <div class="cover-menu">MENU</div>
  </div>
  <div class="art" role="img" aria-label="Drawn spoon and fork" style="left:60px;top:230px;width:160px;height:40px;background:linear-gradient(90deg,#f3f1e6,#c9c1af,#f3f1e6)"></div>
  <div class="cover-title cover-hours" style="top:280px">opened till 5pm</div>
</section>

<section class="page cover cover--pattern">
  <div class="art" role="img" aria-label="Pattern of drawn kitchen utensils" style="inset:0;border-radius:0;background:linear-gradient(160deg,#e3dfd1,#d2cbba)"></div>
  <div class="badge">
    <div class="badge-inner">
      <div class="cover-title cover-name">The Marlowbrook</div>
      <div class="cover-title cover-sub">Breakfast &amp; Lunch</div>
      <div class="cover-title cover-menu">MENU</div>
      <div class="cover-title cover-hours">opened till 5pm</div>
    </div>
  </div>
</section>

</body>
</html>
```